Tilda Tinkerwire, An IT Company Has New Logo, Need Fresh Business Cards

IT company is called Tilda Tinkerwire and is displayed nicely with the new logo from here on pitchloft. Would like a fresh business card look that encompasses the idea that we want clients to Cherish Every Gadget. I love the use of circuitry with hearts as endpoints and x's and o's. It needs to have room for my certification logos of which there are 4 and a BRJ Alumni log. I am attaching my current card to illustrate how it has always captured attention, but that was in the early stages of business when I was doing more residential work. I am focused on businesses now, so a level of professionalism is necessary. I would also like the card to lend itself well to additional stationary, email signature, ticketing template for my workboard, etc. For the time being, I need the card for an upcoming conference so that work will come later. Color scheme should be that of the new logo. Thank you and I look forward to the designs.

Target Market(s)

Businesses looking for IT services.

Industry/Entity Type

Information Technology

Contact Information for Business Card

See above

Requirements
Must have
• New logo colors and a warm feel. Possibly a tad feminine as I am female, but appealing to males.
Nice to have
• I would like techy, but no too much so. I like friendly and connecting feels. People LOVED my old card and called me because it gave them a warm feeling.

```html
<!DOCTYPE html>
<html lang="en">
<head>
<meta charset="utf-8">
<title>Tilda Tinkerwire – Business Card</title>
<link rel="stylesheet" href="https://fonts.googleapis.com/css2?family=Audiowide&family=Comfortaa:wght@400&family=Open+Sans:wght@400;600&display=swap">
<style>
  :root {
    --cyan: #8eeef0;
    --pink: #f4a0ea;
    --lime: #c6ee6e;
    --violet: #c9a2ec;
    --card: #fbfbfb;
    --ghost: #eeeeee;
    --stage: #e6e6e6;
  }
  * { box-sizing: border-box; margin: 0; padding: 0; }
  html, body { width: 1200px; height: 1200px; overflow: hidden; background: var(--stage); }
  .canvas { position: relative; width: 1200px; height: 1200px; }

  .card {
    position: absolute; left: 100px; top: 315px;
    width: 1000px; height: 570px;
    background: linear-gradient(160deg, #ffffff 0%, var(--card) 60%, #f1f1f1 100%);
    box-shadow: 0 18px 40px rgba(0,0,0,.18);
    overflow: hidden;
    font-family: "Open Sans", sans-serif;
  }
  .card__band {
    position: absolute; left: 0; top: 60px; width: 46px; height: 510px;
    background: var(--cyan); border-radius: 0 28px 28px 0;
  }
  .card__device {
    position: absolute; left: 660px; top: 165px; width: 290px; height: 200px;
    background: linear-gradient(135deg, #f0f0f0, var(--ghost));
    border-radius: 22px;
  }

  .call { position: absolute; left: 660px; top: 40px; font-family: "Audiowide", sans-serif; line-height: 1.15; }
  .call__prompt { font-size: 34px; color: var(--cyan); }
  .call__phone { font-size: 32px; color: var(--pink); }

  .brand { position: absolute; left: 110px; top: 165px; }
  .brand__mark { display: flex; align-items: center; gap: 16px; }
  .brand__dot { width: 28px; height: 28px; border-radius: 50%; background: var(--pink); flex: none; }
  .brand__name {
    font-family: "Comfortaa", sans-serif; font-weight: 400; font-size: 54px; color: var(--cyan);
    letter-spacing: -1px; line-height: 1; white-space: nowrap;
  }
  .brand__tagline {
    margin: 14px 0 0 46px; font-size: 15px; letter-spacing: 5px; text-transform: uppercase;
    color: var(--violet); white-space: nowrap;
  }

  .services {
    position: absolute; left: 156px; top: 320px;
    font-size: 24px; font-weight: 600; color: var(--cyan);
    display: flex; align-items: center; gap: 14px;
  }
  .services__sep { width: 22px; height: 22px; }

  .contact {
    position: absolute; top: 420px; display: flex; flex-direction: column; align-items: flex-start; gap: 10px;
    font-size: 22px; color: var(--pink); white-space: nowrap;
  }
  .contact--web { left: 156px; }
  .contact--mail { left: 580px; }
  .contact__icon { width: 34px; height: 34px; }
  .divider { position: absolute; left: 545px; top: 410px; width: 3px; height: 100px; background: var(--lime); }
</style>
</head>
<body>
<main class="canvas">
  <section class="card" aria-label="Tilda Tinkerwire business card">
    <div class="card__band"></div>
    <div class="card__device" role="img" aria-label="Faint desktop computer and tower illustration"></div>

    <div class="call">
      <p class="call__prompt">CALL TILDA!</p>
      <p class="call__phone">407-555-0148</p>
    </div>

    <div class="brand">
      <div class="brand__mark">
        <span class="brand__dot"></span>
        <h1 class="brand__name">Tilda Tinkerwire</h1>
      </div>
      <p class="brand__tagline">× ♡ Cherish Every Gadget ♡ ×</p>
    </div>

    <p class="services">
      <span>Desktops</span>
      <svg class="services__sep" viewBox="0 0 20 20"><path d="M3 3L17 17M17 3L3 17" stroke="var(--pink)" stroke-width="5" stroke-linecap="round"/></svg>
      <span>laptops</span>
      <svg class="services__sep" viewBox="0 0 20 20"><path d="M3 3L17 17M17 3L3 17" stroke="var(--pink)" stroke-width="5" stroke-linecap="round"/></svg>
      <span>tablets</span>
    </p>

    <div class="divider"></div>

    <div class="contact contact--web">
      <svg class="contact__icon" viewBox="0 0 34 34"><rect width="34" height="34" rx="6" fill="var(--cyan)"/><circle cx="17" cy="17" r="10" fill="none" stroke="#fff" stroke-width="2"/><path d="M7 17H27M17 7C12 12 12 22 17 27M17 7C22 12 22 22 17 27" fill="none" stroke="#fff" stroke-width="2"/></svg>
      <span>www.tilda-tinkerwire.com</span>
    </div>

    <div class="contact contact--mail">
      <svg class="contact__icon" viewBox="0 0 34 34"><rect width="34" height="34" rx="6" fill="var(--cyan)"/><rect x="7" y="10" width="20" height="14" fill="none" stroke="#fff" stroke-width="2"/><path d="M7 10L17 18L27 10" fill="none" stroke="#fff" stroke-width="2"/></svg>
      <span>tilda.tinkerwire@mailbox.net</span>
    </div>
  </section>
</main>
</body>
</html>
```